依頼詳細
駅前でチラシを配り集客の確保
記載項目
イタリアンダイニング VELMORA(ヴェルモーラ)東京都中野区中野3−17−9 4F 簡単なMAP
TEL03ー6454−0255 中野に本格イラリアンダイニング オープン!!
オープニング STAFF募集中

サイズ
A5
ページ数
片面
希望イメージ
シンプル 複雑
単色 カラフル
暗い 明るい
日常 高級
遊び心 厳粛
未来的 伝統的
女性的 男性的
希望する色
赤系
納品ファイル
• イラストレーター形式 (.ai)
補足説明
チラシに使う料理ですが4品位
パスタ、ピザ、肉料理、アヒージョなど無料サンプル画像を使って下さい
カジュアル イタリアンダイニング
営業時間 18時から5時
デリカポルト出前出来ます。
追加して下さい
画像を追加して下さい。
メニュー画像

全体のイメージ

チラシのデザイン有難う御座います。

```html
<!DOCTYPE html>
<html lang="ja">
<head>
<meta charset="utf-8">
<title>VELMORA グランドオープン</title>
<link href="https://fonts.googleapis.com/css2?family=Abril+Fatface&family=Noto+Serif+JP:wght@500;700;900&family=Noto+Sans+JP:wght@500;700;900&family=Playfair+Display:ital,wght@0,700;1,700&display=swap" rel="stylesheet">
<style>
  :root {
    --paper: #f3ead8;
    --paper-deep: #e6d8bb;
    --wine: #8a1f16;
    --ink: #3a2418;
    --green: #2f8f3e;
    --red: #c8231d;
    --white: #ffffff;
    --caption: #2b1a12;
  }
  * { margin: 0; padding: 0; box-sizing: border-box; }
  html, body { width: 844px; height: 1200px; overflow: hidden; }
  body { background: var(--paper); font-family: "Noto Sans JP", sans-serif; color: var(--ink); }
  .flyer {
    position: relative; width: 844px; height: 1200px; overflow: hidden;
    background: radial-gradient(ellipse at 50% 40%, #f8f1e3 0%, var(--paper) 60%, var(--paper-deep) 100%);
  }
  .flag-band { position: absolute; left: 0; width: 100%; height: 22px; display: flex; }
  .flag-band span { flex: 1; }
  .flag-band .g { background: var(--green); }
  .flag-band .w { background: transparent; }
  .flag-band .r { background: var(--red); }
  .flag-band.top { top: 0; }
  .flag-band.bottom { bottom: 0; }

  .tagline {
    position: absolute; top: 30px; left: 0; width: 100%; text-align: center;
    font-family: "Noto Serif JP", serif; font-weight: 900; font-size: 27px;
    color: var(--wine); letter-spacing: 1px; white-space: nowrap;
  }
  .headline {
    position: absolute; top: 74px; left: 0; width: 100%; text-align: center;
    font-family: "Abril Fatface", serif; font-size: 108px; line-height: 1;
    color: var(--wine); white-space: nowrap;
  }

  .dish-grid {
    position: absolute; top: 200px; left: 22px; width: 800px;
    display: grid; grid-template-columns: repeat(3, 1fr); grid-template-rows: 300px 300px; gap: 6px;
  }
  .dish { position: relative; overflow: hidden; }
  .dish-lamb { background: linear-gradient(135deg, #5a1d12, #b0482e 55%, #6b3a1f); }
  .dish-pizza { background: linear-gradient(135deg, #e9d2a6, #c9412a 50%, #f1e6cf); }
  .dish-antipasto { background: linear-gradient(135deg, #dcc3a0, #b96a4c 50%, #6d8c3d); }
  .dish-pasta { background: linear-gradient(135deg, #c33a1d, #e06a2c 50%, #f2d39b); }
  .dish-ajillo { background: linear-gradient(135deg, #3a2a22, #e8d9b5 50%, #c24a2b); }
  .dish-gateau { background: linear-gradient(135deg, #f3efe8, #4a2a1d 55%, #e9e3da); }
  .caption {
    position: absolute; bottom: 12px; background: var(--white); color: var(--caption);
    font-weight: 700; font-size: 17px; padding: 4px 12px; border-radius: 6px; line-height: 1.3;
  }
  .caption.center { left: 50%; transform: translateX(-50%); white-space: nowrap; }
  .caption.left { left: 14px; }

  .menu { position: absolute; top: 818px; left: 34px; width: 250px; }
  .menu h2 { font-family: "Noto Serif JP", serif; font-size: 22px; font-weight: 900; color: var(--ink); margin-bottom: 2px; line-height: 1.3; }
  .menu-list { list-style: none; }
  .menu-list li { display: flex; justify-content: space-between; font-size: 15px; font-weight: 700; line-height: 1.55; white-space: nowrap; }
  .staff {
    position: absolute; top: 1030px; left: 34px; width: 250px;
    border: 3px solid var(--red); border-radius: 8px; color: var(--red);
    font-weight: 900; font-size: 17px; text-align: center; padding: 5px 0; white-space: nowrap;
  }
  .delivery {
    position: absolute; top: 1088px; left: 34px; display: flex; align-items: baseline; gap: 8px; white-space: nowrap;
  }
  .delivery .name { font-weight: 900; font-size: 26px; color: var(--ink); }
  .delivery .note { font-weight: 900; font-size: 19px; color: var(--red); }

  .brand { position: absolute; top: 830px; left: 300px; width: 270px; text-align: center; color: var(--ink); }
  .brand-emblem { width: 120px; height: 72px; margin: 0 auto 4px; background: linear-gradient(180deg, #cfc3ae, #9c8a72); border-radius: 6px; opacity: 0.7; }
  .brand-sub { font-family: "Playfair Display", serif; font-style: italic; font-weight: 700; font-size: 20px; line-height: 1.3; }
  .brand-name { font-family: "Playfair Display", serif; font-weight: 700; font-size: 42px; letter-spacing: 3px; line-height: 1.1; }
  .brand-kana { font-weight: 700; font-size: 16px; letter-spacing: 4px; line-height: 1.4; }

  .hours {
    position: absolute; top: 1028px; left: 300px; width: 270px; text-align: center;
    font-weight: 900; font-size: 18px; color: var(--ink); white-space: nowrap;
  }
  .phone {
    position: absolute; top: 1062px; left: 300px; width: 270px; display: flex; align-items: center; justify-content: center; gap: 4px;
    font-weight: 900; font-size: 32px; line-height: 1.2; color: var(--ink); letter-spacing: -0.5px; white-space: nowrap;
  }
  .phone svg { width: 28px; height: 28px; flex: none; }

  .opening-date {
    position: absolute; top: 830px; left: 588px; width: 228px; text-align: center;
    font-weight: 900; font-size: 22px; color: var(--ink); white-space: nowrap;
  }
  .access-map {
    position: absolute; top: 868px; left: 588px; width: 228px; height: 170px;
    background: linear-gradient(180deg, #ffffff, #ece4d4); border: 2px solid var(--ink);
  }
  .address {
    position: absolute; top: 1050px; left: 588px; width: 228px; text-align: right;
    font-weight: 700; font-size: 13px; color: var(--ink); white-space: nowrap;
  }
</style>
</head>
<body>
<main class="flyer">
  <div class="flag-band top"><span class="g"></span><span class="w"></span><span class="r"></span></div>

  <p class="tagline">中野駅北口にカジュアルイタリアンダイニング</p>
  <h1 class="headline">GRAND OPEN</h1>

  <section class="dish-grid">
    <div class="dish dish-lamb" role="img" aria-label="ラム肉のローストの料理写真"><span class="caption center">ラム肉のロースト</span></div>
    <div class="dish dish-pizza" role="img" aria-label="マルゲリータピザの料理写真"><span class="caption center">マルゲリータ</span></div>
    <div class="dish dish-antipasto" role="img" aria-label="前菜の盛り合わせの料理写真"><span class="caption center">前菜の盛り合わせ</span></div>
    <div class="dish dish-pasta" role="img" aria-label="ボロネーゼの料理写真"><span class="caption left">ボロネーゼ</span></div>
    <div class="dish dish-ajillo" role="img" aria-label="丸ごとカマンベールチーズのアヒージョの料理写真"><span class="caption left">丸ごと<br>カマンベールチーズの<br>アヒージョ</span></div>
    <div class="dish dish-gateau" role="img" aria-label="ガトーショコラの料理写真"><span class="caption center">ガトーショコラ</span></div>
  </section>

  <section class="menu">
    <h2>MENU</h2>
    <ul class="menu-list">
      <li><span>生ハム(ハモンセラーノ)</span><span>¥500-</span></li>
      <li><span>ラタトゥイユ</span><span>¥500-</span></li>
      <li><span>農園シーザーサラダ</span><span>¥800-</span></li>
      <li><span>クアトロフォルマッジョ</span><span>¥1,200-</span></li>
      <li><span>カルボナーラ</span><span>¥1,200-</span></li>
      <li><span>牛肉のタリアータ</span><span>¥1,890-</span></li>
      <li><span>ニューヨークチーズケーキ</span><span>¥500-</span></li>
    </ul>
  </section>
  <p class="staff">オープニングSTAFF募集中!</p>
  <p class="delivery"><span class="name">デリカポルト</span><span class="note">ご利用OK</span></p>

  <section class="brand">
    <div class="brand-emblem" role="img" aria-label="木のイラスト"></div>
    <p class="brand-sub">Casual Dining</p>
    <p class="brand-name">VELMORA</p>
    <p class="brand-kana">ヴェルモーラ</p>
  </section>
  <p class="hours">[OPEN] pm18:00~am5:00</p>
  <p class="phone">
    <svg viewBox="0 0 24 24" aria-hidden="true"><path fill="#3a2418" d="M6.6 10.8a15.1 15.1 0 0 0 6.6 6.6l2.2-2.2a1 1 0 0 1 1-.25 11.4 11.4 0 0 0 3.6.57 1 1 0 0 1 1 1V20a1 1 0 0 1-1 1A17 17 0 0 1 3 4a1 1 0 0 1 1-1h3.5a1 1 0 0 1 1 1c0 1.25.2 2.45.57 3.57a1 1 0 0 1-.25 1z"/></svg>
    03-5827-3916
  </p>

  <p class="opening-date">2022.12 OPEN</p>
  <div class="access-map" role="img" aria-label="中野駅北口から店舗までの簡単な地図"></div>
  <p class="address">東京都中野区中野3−17−9 4F</p>

  <div class="flag-band bottom"><span class="g"></span><span class="w"></span><span class="r"></span></div>
</main>
</body>
</html>
```